Luxurious Product label and box for all natural skincare product. + 30AUD tip to winner.

What I require.
1.     One product label and one-box design.
2.     I must have a mock-up of the bottle with the attached label and the box.
 
I have supplied the following files for the designers to use.
1.     Brand logo file. (logo.zip)
2.     Slogan file. (slogan.psd)
3.     Slogan script file. (italianno.regular.ttf)
4.     Bottle image file. (60ml_moisturiser_bottle.png)
5.     Icon bar file. (Icon_bar_en.zip)
 
Label and box Design
I am interested in your unique design concepts and colors, so please feel free to be creative.
1.     Brand name: Quenra
2.     You can use your own choice of colors in your design. I would prefer two colors (excluding logo and slogan colors), although more colors are acceptable for the right design.
3.     Label and box to have a background color or pattern.
4.     I would like the icon bar to wrap around the bottom of the label and box, covering the full width of all sides of the box.
5.     The height of the icon bar should be about 7mm to 10mm high.   
6.     The hex code for the icon bar color is #EDD6D4. The color of the icons can be any color the designer chooses.
7.     The positioning of the icons are as follows.
a)     The front panel has three icons. From left to right, they are; 100% Vegan, Product of Australia, and 100% Natural.
b)     The left side panel has three icons. From the front of the label/box to the back of the label/box, they are; Cruelty-Free, Ethical & Sustainable, and Please Recycle.
c)     The right side panel has only one icon situated at the front of the right side of the label/box. The icon is 6 Months Once Open.
 
Label.
1.     The label will be a three-panel label.
2.     The label will contain text in all three panels; however, only the text for the front panel of the label is supplied in this brief. For now, use Lorem Ipsum placeholder text to fill spaces.
3.     The final text will be provided to the winning designer so they can apply the text to the left and right panels of the label.
4.     Label size. Width 104mm x Height 83mm.
5.     The final design file must include bleed and cut lines.
 
Box.
1.     The box will contain text on all four sides; however, only the text for the front of the box is supplied in this brief. For now, use Lorem Ipsum placeholder text to fill spaces.
2.     The final text will be provided to the winning designer so they can apply the text to the left and right sides and the back of the box.
3.     The box size is 40mm wide x 40mm deep x 140mm high.
4.     The final design file must include bleed and cut lines.
 
Front Panel wording.
1.     Logo.
2.     Slogan.
3.     Moisturiser.
4.     Hydrate & Nourish.
5.     Hyaluronic Acid, Desert Lime & Green Tea.
6.     All Skin Types - Dry – Dehydrated.
7.     Icon bar.
8.     60mL
 
Bottle size
60ml White Bottle – 13.5cm High x 3.5cm Wide.

Target Market(s)

Beauty-minded Asian consumers between the age of 32 and 75 who take a proactive approach in maintaining younger-looking skin. Those who already know the danger of damaged skin caused by skincare containing harsh chemicals, and therefore choose effective natural/organic solutions to meet their skincare needs. Those who wish a more radiant glow and youthful appearance to their skin. Usually, a two-income middle to high-income bracket couple with a mindset for health and beauty.

Industry/Entity Type

Beauty and skincare.

Font styles to use
Other font styles liked:
• Logo and slogan script supplied. Designer to choose all other font or script.

Colors

Designer to choose colors to be used in the design.

Requirements
Must have
• A mock-up label on the bottle and a mock-up box. My logo and slogan are already designed with my chosen font and color.
Nice to have
• I like soft pastel colors with perhaps a small amount of stronger color.

```html
<!DOCTYPE html>
<html lang="en">
<head>
<meta charset="utf-8">
<title>Quenra Moisturiser – Box Dieline and Label</title>
<link rel="stylesheet" href="https://fonts.googleapis.com/css2?family=Montserrat:wght@300;400;500;600;700&family=Italianno&family=Libre+Franklin:wght@400;600;800;900&display=swap">
<style>
:root{
  --stage:#262626;
  --ink:#3b3b3d;
  --line:#2a2a2a;
  --paper:#ffffff;
  --blush:#edd6d4;
  --blush-soft:#f3e4e7;
  --lime:#6fd11a;
  --lime-deep:#3fd100;
  --panel-rule:#9aa0a6;
  --code-box:#2e3236;
}
*{margin:0;padding:0;box-sizing:border-box}
html,body{width:1200px;height:2508px;overflow:hidden;background:var(--stage)}
.canvas{position:relative;width:1200px;height:2508px;background:var(--stage);font-family:'Montserrat',sans-serif;color:var(--ink)}
.artwork{position:absolute;left:0;top:0}
.abs{position:absolute}
.center{text-align:center}

.slogan{font-family:'Italianno',cursive;color:var(--lime);white-space:nowrap;line-height:1}
.brand-name{font-family:'Montserrat',sans-serif;font-weight:400;color:var(--ink);letter-spacing:1px;line-height:1}
.product-type{font-weight:600;letter-spacing:.5px;line-height:1}
.benefit{font-weight:300;line-height:1}
.rule{height:1.5px;background:var(--ink);margin:0 auto}
.detail{font-weight:400;line-height:1.12}
.size{font-weight:400}
.lorem p{margin-bottom:1em}
.lorem p:last-child{margin-bottom:0}

.icon{position:absolute;display:flex;flex-direction:column;align-items:center;transform:translateX(-50%)}
.icon svg{display:block}
.icon span{font-weight:700;text-align:center;line-height:1.1;color:var(--ink);margin-top:2px}

.code-box{background:var(--code-box);color:#fff;display:flex;align-items:center;justify-content:center;font-weight:400}

.nutrition{background:#fff;border:1.5px solid #333;padding:.3em .4em;font-family:'Libre Franklin',sans-serif;color:#2b2b2b;line-height:1.15}
.nutrition h3{font-weight:900;font-size:2.35em;line-height:1;letter-spacing:-.02em;border-bottom:1px solid #333;padding-bottom:.05em}
.nutrition .row{display:flex;justify-content:space-between;border-bottom:1px solid #555;padding:.27em 0}
.nutrition .plain{border:none;padding:.12em 0}
.nutrition .bar-thick{height:.7em;background:#333;margin:.15em 0}
.nutrition .bar-mid{height:.35em;background:#333;margin:.15em 0}
.nutrition .tiny{font-size:.7em;font-weight:800}
.nutrition .calories{font-weight:900;font-size:1.9em;border-bottom:none;padding:0}
.nutrition .dv{justify-content:flex-end;font-size:.75em;font-weight:800}
.nutrition b{font-weight:800}
.nutrition .in1{padding-left:1em}
.nutrition .in2{padding-left:2em}
</style>
</head>
<body>
<div class="canvas">

<svg class="artwork" width="1200" height="2508" viewBox="0 0 1200 2508" aria-hidden="true">
  <defs>
    <linearGradient id="panelFade" x1="0" y1="0" x2="0" y2="1">
      <stop offset="0" stop-color="#ffffff"/>
      <stop offset=".35" stop-color="#ffffff"/>
      <stop offset=".85" stop-color="#f6ecef"/>
      <stop offset="1" stop-color="#f1e0e5"/>
    </linearGradient>
    <linearGradient id="labelFade" x1="0" y1="0" x2="0" y2="1">
      <stop offset="0" stop-color="#ffffff"/>
      <stop offset=".4" stop-color="#ffffff"/>
      <stop offset="1" stop-color="#f5e8ec"/>
    </linearGradient>
    <linearGradient id="limeSweep" x1="0" y1="0" x2="1" y2="0">
      <stop offset="0" stop-color="#7ed321"/>
      <stop offset=".6" stop-color="#43d700"/>
      <stop offset="1" stop-color="#5fe000"/>
    </linearGradient>
  </defs>

  <!-- box flaps -->
  <g fill="#fff" stroke="var(--line)" stroke-width="1.5">
    <path d="M180 406 L107 444 L107 1164 L180 1204 Z"/>
    <path d="M180 406 L193 372 L193 277 L394 277 L394 372 L408 406 Z"/>
    <path d="M635 406 L650 372 L650 277 L848 277 L848 372 L863 406 Z"/>
    <path d="M863 406 L863 200 Q863 152 905 152 L1051 152 Q1093 152 1093 200 L1093 406 Z"/>
    <path d="M180 1204 L193 1240 L193 1325 L394 1325 L394 1240 L408 1204 Z"/>
    <path d="M408 1204 L408 1412 Q408 1457 453 1457 L590 1457 Q635 1457 635 1412 L635 1204 Z"/>
    <path d="M635 1204 L650 1240 L650 1325 L848 1325 L848 1240 L863 1204 Z"/>
  </g>
  <line x1="863" y1="214" x2="1093" y2="214" stroke="var(--line)" stroke-width="1.2"/>
  <path d="M107 1164 L107 1204 L180 1204 Z" fill="#8a8a8a"/>

  <!-- box body -->
  <rect x="180" y="406" width="913" height="798" fill="url(#panelFade)"/>
  <rect x="180" y="1080" width="913" height="124" fill="var(--blush)"/>
  <path d="M180 530 C250 492 350 474 460 472 C600 470 780 472 900 477 C980 482 1050 489 1093 496 L1093 559 C1020 545 940 525 870 512 C800 505 720 540 620 558 C540 545 460 515 386 508 C300 502 230 515 180 534 Z" fill="url(#limeSweep)"/>
  <g stroke="var(--panel-rule)" stroke-width="1">
    <line x1="408" y1="406" x2="408" y2="1204"/>
    <line x1="635" y1="406" x2="635" y2="1204"/>
    <line x1="863" y1="406" x2="863" y2="1204"/>
  </g>
  <rect x="180" y="406" width="913" height="798" fill="none" stroke="var(--line)" stroke-width="1.5"/>

  <!-- label -->
  <rect x="107" y="1569" width="986" height="787" fill="url(#labelFade)"/>
  <rect x="107" y="2186" width="986" height="170" fill="var(--blush)"/>
  <path d="M107 1725 C200 1668 320 1645 450 1644 C600 1643 720 1634 800 1624 L800 1750 C720 1745 640 1722 560 1710 C420 1692 250 1690 107 1742 Z" fill="url(#limeSweep)"/>
</svg>

<!-- ============ BOX : side panel (left) ============ -->
<div class="abs center lorem" style="left:198px;top:579px;width:192px;font-size:12px;line-height:14.4px">
  <p>Lorem ipsum dolor sit amet, consectetuer adipiscing elit, sed diam nonummy nibh euismod tincidunt ut laoreet dolore magna aliquam erat volutpat.</p>
  <p>Lorem ipsum dolor sit amet, consectetuer adipiscing elit, sed diam nonummy nibh euismod tincidunt ut laoreet dolore magna aliquam erat volutpat.</p>
  <p>Lorem ipsum dolor sit amet, consectetuer adipiscing elit, sed diam nonummy nibh euismod tincidunt ut laoreet dolore magna aliquam erat volutpat.</p>
  <p>Lorem ipsum dolor sit amet, consectetuer adipiscing elit, sed diam nonummy nibh euismod tincidunt ut laoreet dolore magna aliquam erat volutpat.</p>
</div>
<div class="icon" style="left:243px;top:1086px;font-size:5px"><svg width="28" height="28" role="img" aria-label="Please recycle icon"><circle cx="14" cy="14" r="11" fill="none" stroke="var(--ink)" stroke-width="1.5"/></svg><span>Please<br>Recycle</span></div>
<div class="icon" style="left:290px;top:1086px;font-size:5px"><svg width="28" height="28" role="img" aria-label="Ethical and sustainable icon"><circle cx="14" cy="14" r="11" fill="none" stroke="var(--ink)" stroke-width="1.5"/></svg><span>Ethical &amp;<br>Sustainable</span></div>
<div class="icon" style="left:336px;top:1086px;font-size:5px"><svg width="28" height="28" role="img" aria-label="Cruelty free icon"><circle cx="14" cy="14" r="11" fill="none" stroke="var(--ink)" stroke-width="1.5"/></svg><span>Cruelty<br>Free</span></div>

<!-- ============ BOX : front panels ============ -->
<div class="abs" style="left:408px;top:406px;width:227px;height:798px">
  <div class="abs slogan" style="right:8px;top:24px;font-size:38px">grown by nature</div>
  <div class="abs center brand-name" style="left:0;width:100%;top:226px;font-size:46px">Quenra</div>
  <div class="abs center product-type" style="left:0;width:100%;top:371px;font-size:19px">MOISTURISER</div>
  <div class="abs center benefit" style="left:0;width:100%;top:398px;font-size:31px;line-height:32px">hydrate &amp;<br>nourish</div>
  <div class="abs rule" style="left:38px;width:151px;top:474px"></div>
  <div class="abs center detail" style="left:0;width:100%;top:482px;font-size:18px;line-height:20px">Hyaluronic Acid<br>Desert Lime &amp;<br>Green Tea.</div>
  <div class="abs rule" style="left:38px;width:151px;top:552px"></div>
  <div class="abs center detail" style="left:0;width:100%;top:562px;font-size:18px;line-height:20px">All Skin Types<br>Dry<br>Dehydrated</div>
  <div class="icon" style="left:47px;top:680px;font-size:5px"><svg width="28" height="28" role="img" aria-label="100% vegan icon"><path d="M14 24 C6 17 3 13 3 9 C3 5 6 3 9 3 C11.5 3 13 5 14 7 C15 5 16.5 3 19 3 C22 3 25 5 25 9 C25 13 22 17 14 24 Z" fill="none" stroke="var(--ink)" stroke-width="1.6"/></svg><span>100%<br>Vegan</span></div>
  <div class="icon" style="left:113px;top:680px;font-size:5px"><svg width="40" height="28" role="img" aria-label="Product of Australia icon"><circle cx="20" cy="14" r="11" fill="none" stroke="var(--ink)" stroke-width="1.5"/></svg><span>Productof<br>Australia</span></div>
  <div class="icon" style="left:180px;top:680px;font-size:5px"><svg width="28" height="28" role="img" aria-label="100% natural icon"><circle cx="14" cy="14" r="11" fill="none" stroke="var(--ink)" stroke-width="1.5"/></svg><span>100%<br>Natural</span></div>
  <div class="abs center size" style="left:0;width:100%;top:742px;font-size:14px">60mL</div>
</div>

<div class="abs" style="left:863px;top:406px;width:230px;height:798px">
  <div class="abs slogan" style="right:10px;top:24px;font-size:38px">grown by nature</div>
  <div class="abs center brand-name" style="left:0;width:100%;top:226px;font-size:46px">Quenra</div>
  <div class="abs center product-type" style="left:0;width:100%;top:371px;font-size:19px">MOISTURISER</div>
  <div class="abs center benefit" style="left:0;width:100%;top:398px;font-size:31px;line-height:32px">hydrate &amp;<br>nourish</div>
  <div class="abs rule" style="left:39px;width:151px;top:474px"></div>
  <div class="abs center detail" style="left:0;width:100%;top:482px;font-size:18px;line-height:20px">Hyaluronic Acid<br>Desert Lime &amp;<br>Green Tea.</div>
  <div class="abs rule" style="left:39px;width:151px;top:552px"></div>
  <div class="abs center detail" style="left:0;width:100%;top:562px;font-size:18px;line-height:20px">All Skin Types<br>Dry<br>Dehydrated</div>
  <div class="icon" style="left:42px;top:680px;font-size:5px"><svg width="28" height="28" role="img" aria-label="100% vegan icon"><path d="M14 24 C6 17 3 13 3 9 C3 5 6 3 9 3 C11.5 3 13 5 14 7 C15 5 16.5 3 19 3 C22 3 25 5 25 9 C25 13 22 17 14 24 Z" fill="none" stroke="var(--ink)" stroke-width="1.6"/></svg><span>100%<br>Vegan</span></div>
  <div class="icon" style="left:112px;top:680px;font-size:5px"><svg width="40" height="28" role="img" aria-label="Product of Australia icon"><circle cx="20" cy="14" r="11" fill="none" stroke="var(--ink)" stroke-width="1.5"/></svg><span>Productof<br>Australia</span></div>
  <div class="icon" style="left:182px;top:680px;font-size:5px"><svg width="28" height="28" role="img" aria-label="100% natural icon"><circle cx="14" cy="14" r="11" fill="none" stroke="var(--ink)" stroke-width="1.5"/></svg><span>100%<br>Natural</span></div>
  <div class="abs center size" style="left:0;width:100%;top:742px;font-size:14px">60mL</div>
</div>

<!-- ============ BOX : back panel ============ -->
<div class="abs nutrition" style="left:652px;top:444px;width:196px;font-size:8.2px">
  <h3>Nutrition Facts</h3>
  <div class="row plain">10 servings per container</div>
  <div class="row plain"><b>Serving size</b><b>1 cup (55g)</b></div>
  <div class="bar-thick"></div>
  <div class="row plain tiny">Amount per serving</div>
  <div class="row calories"><span>Calories</span><span>165</span></div>
  <div class="bar-mid"></div>
  <div class="row dv">% Daily Value*</div>
  <div class="row"><span><b>Total Fat</b> 1.5g</span><b>2%</b></div>
  <div class="row in1"><span>Saturated Fat 0.5g</span><b>3%</b></div>
  <div class="row in1"><span><i>Trans</i> Fat 0g</span><span></span></div>
  <div class="row in1"><span>Polyunsaturated Fat 0.5g</span><span></span></div>
  <div class="row in1"><span>Monounsaturated Fat 0.5g</span><span></span></div>
  <div class="row"><span><b>Cholesterol</b> 0mg</span><b>0%</b></div>
  <div class="row"><span><b>Sodium</b> 180mg</span><b>8%</b></div>
  <div class="row"><span><b>Fluoride</b> 0g</span><span></span></div>
  <div class="row"><span><b>Total Carbohydrate</b> 21g</span><b>8%</b></div>
  <div class="row in1"><span>Dietary Fiber 2g</span><b>7%</b></div>
  <div class="row in2"><span>Soluble Fiber &lt;1g</span><span></span></div>
  <div class="row in2"><span>Insoluble Fiber 1g</span><span></span></div>
  <div class="row in1 plain"><span>Total Sugars 8g</span><span></span></div>
</div>
<div class="abs center lorem" style="left:650px;top:778px;width:198px;font-size:10.4px;line-height:12.8px">
  <p style="margin-bottom:1.4em">Lorem ipsum dolor sit amet, consectetuer adipiscing elit, sed diam nonummy nibh euismod tincidunt ut laoreet dolore magna aliquam erat volutpat.</p>
  <p style="margin-bottom:1.4em">Lorem ipsum dolor sit amet, consectetuer adipiscing elit, sed diam nonummy nibh euismod tincidunt ut laoreet dolore magna aliquam erat volutpat.</p>
  <p style="margin-bottom:1.4em">Lorem ipsum dolor sit amet, consectetuer adipiscing elit, sed diam nonummy nibh euismod tincidunt ut laoreet dolore magna aliquam erat volutpat.</p>
  <p>Lorem ipsum dolor sit amet, consectetuer adipiscing elit, sed diam nonummy nibh euismod tincidunt ut laoreet dolore magna aliquam erat volutpat.</p>
</div>
<div class="abs code-box" style="left:655px;top:1089px;width:132px;height:71px;font-size:16px">bar code</div>
<div class="icon" style="left:811px;top:1090px;font-size:5px"><svg width="24" height="22" role="img" aria-label="6 months once open icon"><rect x="3" y="4" width="18" height="15" rx="2" fill="none" stroke="var(--ink)" stroke-width="1.4"/><text x="12" y="15" text-anchor="middle" font-family="Montserrat,sans-serif" font-size="7" font-weight="600" fill="#3b3b3d">6M</text></svg><span>6 Months<br>Once Open</span></div>

<!-- ============ LABEL ============ -->
<div class="abs center lorem" style="left:148px;top:1753px;width:246px;font-size:15px;line-height:17px">
  <p style="margin-bottom:1.15em">Lorem ipsum dolor sit amet, consectetuer adipiscing elit, sed diam nonummy nibh euismod tincidunt ut laoreet dolore magna aliquam erat volutpat.</p>
  <p style="margin-bottom:1.15em">Lorem ipsum dolor sit amet, consectetuer adipiscing elit, sed diam nonummy nibh euismod tincidunt ut laoreet dolore magna aliquam erat volutpat.</p>
  <p style="margin-bottom:1.15em">Lorem ipsum dolor sit amet, consectetuer adipiscing elit, sed diam nonummy nibh euismod tincidunt ut laoreet dolore magna aliquam erat volutpat.</p>
  <p>Lorem ipsum dolor sit amet, consectetuer adipiscing elit, sed diam nonummy nibh euismod tincidunt ut laoreet dolore magna aliquam erat volutpat.</p>
</div>

<div class="abs slogan" style="left:494px;top:1592px;font-size:44px">grown by nature</div>
<div class="abs center brand-name" style="left:440px;width:316px;top:1800px;font-size:68px">Quenra</div>
<div class="abs center product-type" style="left:440px;width:316px;top:1953px;font-size:31px;font-weight:700">MOISTURISER</div>
<div class="abs center" style="left:440px;width:316px;top:1987px;font-size:19px;font-weight:600">Hydrate &amp; Nourish</div>
<div class="abs rule" style="left:466px;width:266px;top:2022px"></div>
<div class="abs center detail" style="left:440px;width:316px;top:2033px;font-size:20px;line-height:24px">Hyaluronic Acid<br>Desert Lime &amp; Green Tea.</div>
<div class="abs rule" style="left:466px;width:266px;top:2093px"></div>
<div class="abs center detail" style="left:440px;width:316px;top:2104px;font-size:20px;line-height:24px">All Skin Types<br>Dry – Dehydrated</div>

<div class="abs nutrition" style="left:789px;top:1623px;width:278px;font-size:11.6px">
  <h3>Nutrition Facts</h3>
  <div class="row plain">10 servings per container</div>
  <div class="row plain"><b>Serving size</b><b>1 cup (55g)</b></div>
  <div class="bar-thick"></div>
  <div class="row plain tiny">Amount per serving</div>
  <div class="row calories"><span>Calories</span><span>165</span></div>
  <div class="bar-mid"></div>
  <div class="row dv">% Daily Value*</div>
  <div class="row"><span><b>Total Fat</b> 1.5g</span><b>2%</b></div>
  <div class="row in1"><span>Saturated Fat 0.5g</span><b>3%</b></div>
  <div class="row in1"><span><i>Trans</i> Fat 0g</span><span></span></div>
  <div class="row in1"><span>Polyunsaturated Fat 0.5g</span><span></span></div>
  <div class="row in1"><span>Monounsaturated Fat 0.5g</span><span></span></div>
  <div class="row"><span><b>Cholesterol</b> 0mg</span><b>0%</b></div>
  <div class="row"><span><b>Sodium</b> 180mg</span><b>8%</b></div>
  <div class="row"><span><b>Fluoride</b> 0g</span><span></span></div>
  <div class="row"><span><b>Total Carbohydrate</b> 21g</span><b>8%</b></div>
  <div class="row in1"><span>Dietary Fiber 2g</span><b>7%</b></div>
  <div class="row in2"><span>Soluble Fiber &lt;1g</span><span></span></div>
  <div class="row in2"><span>Insoluble Fiber 1g</span><span></span></div>
  <div class="row in1 plain"><span>Total Sugars 8g</span><span></span></div>
</div>
<div class="abs center lorem" style="left:805px;top:2072px;width:252px;font-size:14.5px;line-height:17px">
  <p>Lorem ipsum dolor sit amet, consectetuer adipiscing elit, sed diam nonummy nibh euismod tincidunt ut laoreet dolore magna aliquam erat volutpat.</p>
</div>

<div class="icon" style="left:193px;top:2196px;font-size:9.5px"><svg width="46" height="44" role="img" aria-label="Please recycle icon"><circle cx="23" cy="22" r="18" fill="none" stroke="var(--ink)" stroke-width="2"/></svg><span>Please<br>Recycle</span></div>
<div class="icon" style="left:271px;top:2196px;font-size:9.5px"><svg width="46" height="44" role="img" aria-label="Ethical and sustainable icon"><circle cx="23" cy="22" r="18" fill="none" stroke="var(--ink)" stroke-width="2"/></svg><span>Ethical &amp;<br>Sustainable</span></div>
<div class="icon" style="left:345px;top:2196px;font-size:9.5px"><svg width="46" height="44" role="img" aria-label="Cruelty free icon"><circle cx="23" cy="22" r="18" fill="none" stroke="var(--ink)" stroke-width="2"/></svg><span>Cruelty<br>Free</span></div>
<div class="icon" style="left:484px;top:2196px;font-size:9.5px"><svg width="46" height="44" role="img" aria-label="100% vegan icon"><path d="M23 40 C10 29 5 22 5 15 C5 8 10 4 15 4 C19 4 21.5 7 23 10 C24.5 7 27 4 31 4 C36 4 41 8 41 15 C41 22 36 29 23 40 Z" fill="none" stroke="var(--ink)" stroke-width="2.4"/></svg><span>100%<br>Vegan</span></div>
<div class="icon" style="left:600px;top:2196px;font-size:9.5px"><svg width="70" height="44" role="img" aria-label="Product of Australia icon"><circle cx="35" cy="22" r="18" fill="none" stroke="var(--ink)" stroke-width="2"/></svg><span>Productof<br>Australia</span></div>
<div class="icon" style="left:707px;top:2196px;font-size:9.5px"><svg width="46" height="44" role="img" aria-label="100% natural icon"><circle cx="23" cy="22" r="18" fill="none" stroke="var(--ink)" stroke-width="2"/></svg><span>100%<br>Natural</span></div>
<div class="abs center size" style="left:500px;width:200px;top:2300px;font-size:22px">60mL</div>
<div class="abs code-box" style="left:799px;top:2203px;width:186px;height:99px;font-size:15px">bar code</div>
<div class="icon" style="left:1035px;top:2200px;font-size:9.5px"><svg width="36" height="36" role="img" aria-label="6 months once open icon"><rect x="5" y="6" width="26" height="24" rx="3" fill="none" stroke="var(--ink)" stroke-width="2"/><text x="18" y="23" text-anchor="middle" font-family="Montserrat,sans-serif" font-size="10" font-weight="600" fill="#3b3b3d">6M</text></svg><span>6 Months<br>Once Open</span></div>

</div>
</body>
</html>
```